Company Profile for Consulting Comany

Need Company profile to be designed in a professional way.

for inspiring :-
https://www.folivane.net/gallery/5372904/COMPANY-PROFILE
https://www.folivane.net/gallery/60391742/Biotech-Product-Catalog-No1-(Laminar-Air-Flow)
https://www.folivane.net/gallery/73905218/MPG-Globalpath-Company-Profile-2014-(MPG-Rebrand-part-2)

Target Market(s)

Corporate

Industry/Entity Type

It Company

Font styles to use
Sans Serif

Requirements
Must have
• Landscape A4 size
• Must go with the logo branding
• Must Have Visual Identity is the most important
• Must Have mpty spaces

```html
<!DOCTYPE html>
<html lang="en">
<head>
<meta charset="utf-8">
<title>Pivot Path – Company Profile Pages</title>
<link href="https://fonts.googleapis.com/css2?family=Quicksand:wght@400;500;600;700&family=Open+Sans:wght@400;600;700&display=swap" rel="stylesheet">
<style>
:root{
  --board:#c4996b;
  --label:#ffffff;
  --page-a:#48484b;
  --page-b:#2c2c2e;
  --panel:rgba(88,112,122,.72);
  --bar:#b8bbbd;
  --bar-light:#dcdedf;
  --teal:#2aa6d6;
  --footer:#0a0a0a;
  --ink:#e9eced;
  --ink-soft:#c9d0d3;
  --dark:#222;
  --value-row:#4d8fcf;
}
*{box-sizing:border-box;margin:0;padding:0}
html,body{width:1200px;height:907px;overflow:hidden}
body{background:var(--board);font-family:"Open Sans",Arial,sans-serif;position:relative;color:var(--ink)}

.board-label{position:absolute;font-family:"Open Sans",Arial,sans-serif;font-weight:700;font-size:19px;color:var(--label);text-align:center;width:530px}

.page{position:absolute;width:530px;height:374px;overflow:hidden;
  background:radial-gradient(ellipse at 50% 35%,var(--page-a) 0%,#3a3a3c 45%,var(--page-b) 100%);
  box-shadow:2px 3px 6px rgba(0,0,0,.45)}
.strip{position:absolute;left:0;right:0;height:16px;top:285px;
  background:linear-gradient(#5a5a5c,#9a9a9c 40%,#6a6a6c 70%,#3a3a3c)}
.strip::after{content:"";position:absolute;inset:0;
  background:radial-gradient(circle at 15% 50%,rgba(255,255,255,.8) 0,transparent 8%),
  radial-gradient(circle at 50% 50%,rgba(255,255,255,.8) 0,transparent 8%),
  radial-gradient(circle at 85% 50%,rgba(255,255,255,.8) 0,transparent 8%)}
.footer{position:absolute;left:0;right:0;top:301px;height:65px;background:var(--footer)}
.edge{position:absolute;left:0;right:0;bottom:0;height:8px;background:linear-gradient(#666,#3a3a3a)}
.page.lower .strip{top:320px;height:13px}
.page.lower .footer{top:333px;height:34px}
.page.lower .edge{height:7px}

.brand{position:absolute;display:flex;flex-direction:column;align-items:center}
.brand .rule{width:100%;height:3px;background:linear-gradient(90deg,#777,#ddd,#777)}
.brand .name{display:flex;align-items:center;gap:6px;font-family:"Quicksand",sans-serif;font-weight:700;color:var(--teal);line-height:1}
.brand .mark{display:inline-block;background:var(--teal)}
.brand .tag{align-self:flex-end;font-size:5.5px;letter-spacing:1.4px;color:#9aa;margin:1px 6px 2px 0}

.hero-name{position:absolute;display:flex;align-items:center;gap:14px;font-family:"Quicksand",sans-serif;font-weight:700;color:#9a9c9e}
.hero-name .mark{display:inline-block;background:var(--teal)}

.tagline-small{position:absolute;font-family:"Quicksand",sans-serif;color:#b8b8b8;letter-spacing:.5px}
.tagline-big{position:absolute;font-family:"Quicksand",sans-serif;font-weight:400;color:#dcdcdc}

.page-title{position:absolute;font-family:"Quicksand",sans-serif;font-weight:500;color:#f2f2f2;font-size:18px}
.pillars{position:absolute;font-family:"Quicksand",sans-serif;font-weight:600;color:var(--teal);font-size:11.5px}
.pillars span{color:#888;margin:0 3px;font-weight:400}
.folio{position:absolute;width:15px;height:15px;border-radius:50%;background:#eee;color:#222;font-size:8px;font-weight:700;display:flex;align-items:center;justify-content:center;box-shadow:0 0 0 2px #777}

.panel{position:absolute;background:var(--panel)}
.why{left:18px;top:46px;width:238px;height:234px;padding:5px 5px;display:flex;flex-direction:column;gap:4px}
.why h3{background:var(--bar);color:#fff;font-weight:400;font-size:7.5px;padding:1px 4px;line-height:10px}
.why p{font-size:5.2px;line-height:8.5px;color:var(--ink-soft);text-align:justify;padding:1px 4px 0}

.photo{position:absolute;width:116px;height:72px;border:2px solid #f2f2f2}

.toc{left:22px;top:9px;width:238px;height:302px;padding:5px 5px;font-size:6.3px}
.toc .row{display:flex;justify-content:space-between;height:11.2px;align-items:center;padding:0 4px}
.toc .head{background:var(--bar-light);color:var(--dark);font-weight:700;margin-top:2px}
.toc .head b{color:#fff;font-weight:400}
.toc .sub{color:#eef;padding-left:18px;height:9.6px}
.toc .sub span:last-child{color:#ccc}

.who{left:22px;top:45px;width:482px;height:148px;padding:8px;display:flex;gap:14px}
.who .col-a{width:236px}
.who .col-b{flex:1}
.who h3{font-size:8.5px;font-weight:700;color:#fff;margin-bottom:4px}
.who p{font-size:5.2px;line-height:8.7px;color:var(--ink-soft);text-align:justify}
.who ul{list-style:none;margin-top:6px}
.who li{font-size:5.2px;line-height:8px;color:var(--ink-soft);display:flex;gap:4px;margin-bottom:4px}
.who li::before{content:"";flex:0 0 6px;height:6px;border-radius:50%;background:#fff;margin-top:1px}

.values{position:absolute;left:22px;top:208px;width:482px;font-size:5.3px}
.values .vhead{background:#7c7f81;color:#fff;font-weight:700;font-size:8.5px;height:19px;display:flex;align-items:center;padding-left:8px;border-right:1px solid #aaa}
.values .vrow{display:flex;background:var(--value-row);height:12px;align-items:center;border-top:1px solid rgba(255,255,255,.25)}
.values .vkey{width:122px;display:flex;align-items:center;gap:4px;padding-left:8px;font-weight:700;color:#fff;border-right:1px solid rgba(255,255,255,.5);height:100%}
.values .vtext{padding-left:8px;color:#eef4fb}
</style>
</head>
<body>

<div class="board-label" style="left:32px;top:38px">Front Cover</div>
<div class="board-label" style="left:621px;top:39px">Page 3 (Inside page)</div>
<div class="board-label" style="left:32px;top:842px">Page 1 (Content page)</div>
<div class="board-label" style="left:621px;top:839px">Page 2 (Inside page)</div>

<!-- Front cover -->
<section class="page cover" style="left:58px;top:70px">
  <div class="hero-name" style="left:118px;top:138px;font-size:40px"><span class="mark" style="width:30px;height:30px"></span>Pivot Path</div>
  <div class="strip"></div>
  <div class="footer">
    <div class="tagline-small" style="left:81px;top:14px;font-size:9.5px">WE CAN HELP YOU TO</div>
    <div class="tagline-big" style="left:30px;top:32px;font-size:17.5px">MAKE CHANGE HAPPEN</div>
    <div class="brand" style="left:296px;top:8px;width:210px">
      <div class="rule"></div>
      <div class="name" style="font-size:17px;margin-top:6px"><span class="mark" style="width:12px;height:12px"></span>Pivot Path</div>
      <div class="tag">A PATH TO CHANGE</div>
      <div class="rule"></div>
    </div>
  </div>
  <div class="edge"></div>
</section>

<!-- Page 3 -->
<section class="page" style="left:602px;top:70px">
  <h2 class="page-title" style="left:20px;top:16px">Why Pivot Path?</h2>
  <div class="panel why">
    <h3>Success</h3>
    <p>We will deliver reliable results for you, as our services record shows. In the past few years, we have helped a numbers of organizations with a less than 2% rejection rate.</p>
    <h3>Targeting</h3>
    <p>We understand the importance of targeting the right people and community, the right way. We will work with you to understand the importance of communication and how you can focus the right individual at a good time.</p>
    <h3>Superior Workforce</h3>
    <p>Our dedicated training professionals have all been rigorously screened and training to perform at their peak level. They know that they represent our company at all times and understand the importance of enhancing your image.</p>
    <h3>Flexible Multichannel Abilities</h3>
    <p>Our wide capabilities give an extensive reach and the ability to create exactly the right program and deliver it where it will get the best results.</p>
    <h3>Cost Effectiveness</h3>
    <p>Pivot Path will train your staff by offering very affordable value-added projects</p>
  </div>
  <div class="photo" role="img" aria-label="Photo of a business team standing in a bright office" style="left:269px;top:46px;background:linear-gradient(135deg,#dfe3e6,#9aa4ad 60%,#5e6a75)"></div>
  <div class="photo" role="img" aria-label="Photo of a smiling businesswoman with colleagues behind" style="left:393px;top:46px;background:linear-gradient(135deg,#eef0f2,#b7bcc2 55%,#4a4f57)"></div>
  <div class="photo" role="img" aria-label="Photo of a business meeting around a table" style="left:269px;top:126px;background:linear-gradient(135deg,#e6eaee,#8f9cab 55%,#3f4c5c)"></div>
  <div class="photo" role="img" aria-label="Photo of a businesswoman at a meeting with colleagues" style="left:393px;top:126px;background:linear-gradient(135deg,#f0ece6,#c4b9ac 55%,#6b6259)"></div>
  <div class="photo" role="img" aria-label="Photo of a team applauding at a seminar" style="left:269px;top:205px;background:linear-gradient(135deg,#ebe7e2,#b4aaa0 55%,#6a5a50)"></div>
  <div class="photo" role="img" aria-label="Photo of a businesswoman in an office corridor" style="left:393px;top:205px;background:linear-gradient(135deg,#dbe4ee,#93a7bd 55%,#4d5a6a)"></div>
  <div class="strip"></div>
  <div class="footer">
    <div class="pillars" style="left:16px;top:41px">strategy<span>|</span>people<span>|</span>technology</div>
    <div class="folio" style="left:252px;top:40px">3</div>
    <div class="brand" style="left:296px;top:8px;width:210px">
      <div class="rule"></div>
      <div class="name" style="font-size:17px;margin-top:6px"><span class="mark" style="width:12px;height:12px"></span>Pivot Path</div>
      <div class="tag">A PATH TO CHANGE</div>
      <div class="rule"></div>
    </div>
  </div>
  <div class="edge"></div>
</section>

<!-- Page 1 -->
<section class="page lower" style="left:58px;top:461px">
  <nav class="panel toc">
    <div class="row head"><span>Who we are?</span><b>2</b></div>
    <div class="row sub"><span>Executive Summary</span><span>2</span></div>
    <div class="row sub"><span>Vision</span><span>2</span></div>
    <div class="row sub"><span>Mission</span><span>2</span></div>
    <div class="row sub"><span>Values</span><span>2</span></div>
    <div class="row head"><span>Why Pivot Path?</span><b>3</b></div>
    <div class="row head"><span>What we do?</span><b>4</b></div>
    <div class="row sub"><span>HR &amp; OD Consultation</span><span>4</span></div>
    <div class="row sub"><span>Professional Training</span><span>4</span></div>
    <div class="row sub"><span>Talent Assessment</span><span>5</span></div>
    <div class="row sub"><span>HR Solutions</span><span>5</span></div>
    <div class="row head"><span>Partnership</span><b>6</b></div>
    <div class="row sub"><span>Arbor Change Partners, Inc.</span><span>6</span></div>
    <div class="row sub"><span>Marwick Halden</span><span>6</span></div>
    <div class="row sub"><span>brightroster</span><span>6</span></div>
    <div class="row sub"><span>Veltria Consulting</span><span>6</span></div>
    <div class="row head"><span>Our Team</span><b>7</b></div>
    <div class="row sub"><span>Karim Al Nouri Consulting Manager</span><span>7</span></div>
    <div class="row sub"><span>Tariq Mansour Assoc. Consultant</span><span>7</span></div>
    <div class="row sub"><span>Hisham Al-Sayed Projects Manager</span><span>8</span></div>
    <div class="row sub"><span>Nabil Osman Assoc. Consultant</span><span>8</span></div>
    <div class="row head" style="margin-top:5px"><span>Certifications</span><b>9</b></div>
    <div class="row head" style="margin-top:5px"><span>Our Clients</span><b>10</b></div>
    <div class="row head" style="margin-top:5px"><span>Contact us</span><b>11</b></div>
  </nav>
  <h2 class="page-title" style="left:322px;top:16px">Table of Contents</h2>
  <div class="hero-name" style="left:316px;top:150px;font-size:24px;gap:8px"><span class="mark" style="width:18px;height:18px"></span>Pivot Path</div>
  <div class="strip"></div>
  <div class="footer">
    <div class="tagline-small" style="left:56px;top:6px;font-size:6.5px">WE CAN HELP YOU TO</div>
    <div class="tagline-big" style="left:22px;top:17px;font-size:12px">MAKE CHANGE HAPPEN</div>
    <div class="brand" style="left:330px;top:2px;width:142px">
      <div class="rule" style="height:2px"></div>
      <div class="name" style="font-size:11.5px;margin-top:5px;gap:4px"><span class="mark" style="width:8px;height:8px"></span>Pivot Path</div>
      <div class="tag" style="font-size:4px;letter-spacing:1px">A PATH TO CHANGE</div>
      <div class="rule" style="height:2px"></div>
    </div>
  </div>
  <div class="edge"></div>
</section>

<!-- Page 2 -->
<section class="page lower" style="left:602px;top:461px">
  <h2 class="page-title" style="left:22px;top:10px">Who We Are?</h2>
  <div class="panel who">
    <div class="col-a">
      <h3>Executive Summary</h3>
      <p>Pivot Path is professional HR &amp; OD Organization, which is Specialized in Talent and Organizational Development, Career Coaching, Leadership Assessment and Development, Total Reward, HR Technology &amp; providing a wide range of outsourcing payroll and recruitment services with a vision to be the leading HR outsourcing company in the Middle East. Pivot Path is a local house of HR &amp; OD expertise with global experience, driven by one thought, to raise the bar of local HR practices and knowledge. Pivot Path have developed partnerships with various companies and organizations, among those brightroster will be the strategic partner to provide HR outsourcing services through their platforms.</p>
      <h3 style="margin-top:7px">Vision</h3>
      <p>"To become the leading HR outsourcing company in the Middle East and stand known of quality services."</p>
    </div>
    <div class="col-b">
      <h3>Mission</h3>
      <p>We have a multi-layered mission statement catering for the needs of our customers in addition to increasing the value of our services and upgrading our standing among our competitors. Our missions are:</p>
      <ul>
        <li>To provide convenient HR solutions to SMEs so they can focus on the core of their business.</li>
        <li>To play our role in economic development of Saudi Arabia and other Middle East countries.</li>
        <li>To develop a professional relationship with our valued clientele and investors.</li>
        <li>To bring innovation in HR services through technology.</li>
      </ul>
    </div>
  </div>
  <table class="values" role="presentation" style="display:block">
    <tbody style="display:block">
    <tr class="vhead" style="display:flex"><th style="font-weight:700">Values</th></tr>
    </tbody>
  </table>
  <div class="values" style="top:227px">
    <div class="vrow"><div class="vkey"><svg width="6" height="6" viewBox="0 0 10 10"><circle cx="5" cy="5" r="5" fill="#fff"/><path d="M2.5 5.2l1.8 1.8 3.3-3.6" stroke="#4d8fcf" stroke-width="1.6" fill="none"/></svg>INTEGRITY:</div><div class="vtext">Pivot Path will ensure integrity within employees and with clients, investors and strategic partners.</div></div>
    <div class="vrow"><div class="vkey"><svg width="6" height="6" viewBox="0 0 10 10"><circle cx="5" cy="5" r="5" fill="#fff"/><path d="M2.5 5.2l1.8 1.8 3.3-3.6" stroke="#4d8fcf" stroke-width="1.6" fill="none"/></svg>WORKPLACE ENTERTAINMENT:</div><div class="vtext">Pivot Path will provide enjoyment of all employees at the workplace to promote work as a passion instead of a profession.</div></div>
    <div class="vrow"><div class="vkey"><svg width="6" height="6" viewBox="0 0 10 10"><circle cx="5" cy="5" r="5" fill="#fff"/><path d="M2.5 5.2l1.8 1.8 3.3-3.6" stroke="#4d8fcf" stroke-width="1.6" fill="none"/></svg>ACCOUNTABILITY:</div><div class="vtext">In Pivot Path, from MD to staff everyone will be accountable for their actions and decision.</div></div>
    <div class="vrow"><div class="vkey"><svg width="6" height="6" viewBox="0 0 10 10"><circle cx="5" cy="5" r="5" fill="#fff"/><path d="M2.5 5.2l1.8 1.8 3.3-3.6" stroke="#4d8fcf" stroke-width="1.6" fill="none"/></svg>PURSUIT OF EXCELLENCE:</div><div class="vtext">Each employee and stakeholder will strive for excellence in his role and professional activities.</div></div>
    <div class="vrow"><div class="vkey"><svg width="6" height="6" viewBox="0 0 10 10"><circle cx="5" cy="5" r="5" fill="#fff"/><path d="M2.5 5.2l1.8 1.8 3.3-3.6" stroke="#4d8fcf" stroke-width="1.6" fill="none"/></svg>QUALITY CONTROL:</div><div class="vtext">Pivot Path will implement strict quality control to improve the standard of its services continuously.</div></div>
    <div class="vrow"><div class="vkey"><svg width="6" height="6" viewBox="0 0 10 10"><circle cx="5" cy="5" r="5" fill="#fff"/><path d="M2.5 5.2l1.8 1.8 3.3-3.6" stroke="#4d8fcf" stroke-width="1.6" fill="none"/></svg>AFFORDABILITY:</div><div class="vtext">Services of Pivot Path will be affordable to meet the demands of local companies.</div></div>
  </div>
  <div class="strip"></div>
  <div class="footer">
    <div class="pillars" style="left:25px;top:11px;font-size:11px">strategy<span>|</span>people<span>|</span>technology</div>
    <div class="folio" style="left:258px;top:9px">2</div>
    <div class="brand" style="left:330px;top:2px;width:142px">
      <div class="rule" style="height:2px"></div>
      <div class="name" style="font-size:11.5px;margin-top:5px;gap:4px"><span class="mark" style="width:8px;height:8px"></span>Pivot Path</div>
      <div class="tag" style="font-size:4px;letter-spacing:1px">A PATH TO CHANGE</div>
      <div class="rule" style="height:2px"></div>
    </div>
  </div>
  <div class="edge"></div>
</section>

</body>
</html>
```